Friendly, Professional, Simple Catering Menu

Currently we cater but don't have a take-out menu for customers to order from or see our options and we want to change that. Most of the customers we cater are employees of large and small businesses, we also have some private parties we cater to as well. With this in mind we are looking for a professional looking menu but also to have some personal touch with it. The format should be easy to read and understand. We are looking to hand out this menu to local businesses, schools and offices, and maybe after a few trial runs, our store too. Locally, we have a pretty established name but our options can't be seen by the public and we are looking to make that possible with this catering menu. Originally we were thinking of tri-fold menu, 8.5inx14in, but after seeing some of the work done already we trust the designers to create something they think would be the right fit. We don't want it too large nor too small to ensure it won't be an inconvenience for businesses, it must still stand out enough to grab their attention.
Target Market(s)
Businesses, Schools, Office buildings, and Private parties.
Industry/Entity Type
Catering

```html
<!DOCTYPE html>
<html lang="en">
<head>
<meta charset="utf-8">
<title>Ladle and Loaf Catering Menu</title>
<link rel="stylesheet" href="https://fonts.googleapis.com/css2?family=Sniglet&family=Open+Sans:wght@400;600&display=swap">
<style>
:root{
  --cream:#fcf0c0;
  --cream-deep:#f7e3a2;
  --wood-light:#ece5dc;
  --wood-mid:#ddd3c6;
  --red:#e5262b;
  --ink:#222;
  --dark:#3a2a25;
}
*{margin:0;padding:0;box-sizing:border-box}
html,body{width:1200px;height:729px;overflow:hidden}
body{font-family:"Open Sans",Arial,sans-serif;font-size:12px;color:var(--ink);line-height:1.3}
.menu{position:relative;width:1200px;height:729px;
  background:repeating-linear-gradient(90deg,var(--wood-light) 0 58px,var(--wood-mid) 58px 60px,#f2ece4 60px 120px,var(--wood-mid) 120px 122px);}
.inside{position:absolute;left:0;top:0;width:810px;height:697px;
  background:radial-gradient(ellipse at 40% 40%,#fdf4cf,var(--cream) 60%,var(--cream-deep));}
.t{position:absolute;white-space:nowrap;font-weight:400}
.heading{font-family:"Sniglet",cursive;font-weight:400;color:var(--red);font-size:29px;line-height:1;transform:translateX(-50%)}
.red{color:var(--red)}
.bul{padding-left:12px}
.bul::before{content:"";position:absolute;left:2px;top:7px;width:4px;height:4px;border-radius:50%;background:var(--ink)}
.photo{position:absolute;border-radius:14px}
.partner-badge{position:absolute;left:576px;top:224px;width:94px;height:94px;border-radius:50%;background:var(--dark)}
.divider{position:absolute;left:589px;top:532px;width:2px;height:78px;background:var(--ink)}
.brand{position:absolute;left:1001px;top:131px;transform:translate(-50%,-50%);font-family:"Sniglet",cursive;font-weight:400;font-size:44px;color:var(--red);line-height:1;text-align:center;white-space:nowrap}
.site{position:absolute;left:1010px;top:657px;transform:translateX(-50%);font-size:19px;color:#333;white-space:nowrap}
</style>
</head>
<body>
<main class="menu">
  <section class="inside">
    <h2 class="t heading" style="left:178px;top:22px">Sandwiches</h2>
    <p class="t red" style="left:12px;top:66px">Choose one Bread, Meat, and Cheese.</p>
    <p class="t red" style="left:12px;top:85px">Bread</p>
    <p class="t" style="left:12px;top:102px">White Bread, Wheat Bread, and Sourdough Bread</p>
    <p class="t red" style="left:12px;top:120px">Meats</p>
    <p class="t" style="left:12px;top:137px">Ham, Turkey, Roast Beef</p>
    <p class="t red" style="left:12px;top:155px">Cheeses</p>
    <p class="t" style="left:12px;top:173px">Cheddar, Provolone, and Swiss</p>
    <p class="t" style="left:62px;top:197px">Small</p><p class="t" style="left:122px;top:197px">$37.99</p><p class="t" style="left:173px;top:197px">(serves 5-10)</p>
    <p class="t" style="left:62px;top:217px">Medium</p><p class="t" style="left:122px;top:217px">$54.99</p><p class="t" style="left:173px;top:217px">(serves 11-15)</p>
    <p class="t" style="left:62px;top:236px">Large</p><p class="t" style="left:122px;top:236px">$69.99</p><p class="t" style="left:173px;top:236px">(serves 16-20)</p>
    <div class="photo" role="img" aria-label="Platter of assorted sandwiches" style="left:12px;top:262px;width:179px;height:110px;background:linear-gradient(135deg,#d9b48a,#a2392f 70%,#7a2a25)"></div>
    <div class="photo" role="img" aria-label="Row of soup kettles on a buffet" style="left:208px;top:262px;width:181px;height:110px;background:linear-gradient(135deg,#6d5844,#b07a45 50%,#4a3a2c)"></div>

    <h2 class="t heading" style="left:169px;top:386px">Combo</h2>
    <p class="t red" style="left:12px;top:416px">Ladle and Loaf to you</p>
    <p class="t bul" style="left:26px;top:436px">Minimum 25 people</p>
    <p class="t bul" style="left:26px;top:455px">3 Soups of their choice</p>
    <p class="t bul" style="left:26px;top:474px">PortableSalad Bar</p>
    <p class="t bul" style="left:26px;top:493px">All you can eat Breadsticks</p>
    <p class="t bul" style="left:26px;top:516px">We do delivery, set up, and clean up</p>
    <p class="t bul" style="left:26px;top:535px">$8.49 per a person</p>

    <h2 class="t heading" style="left:179px;top:554px">Extras</h2>
    <p class="t" style="left:12px;top:588px"><span class="red">Pasta Salads</span>&nbsp; $1.49 per serving</p>
    <p class="t" style="left:83px;top:606px">$19.99 Family Size (Approx. 5lbs)</p>
    <p class="t bul" style="left:26px;top:625px">Potato Salad</p>
    <p class="t bul" style="left:26px;top:644px">Spaghetti Salad</p>
    <p class="t bul" style="left:26px;top:662px">Italian Rotini Pasta Salad</p>
    <p class="t bul" style="left:26px;top:679px">Springtime Bowtie Pasta Salad</p>

    <p class="t bul" style="left:424px;top:10px">Chicken Parmesan Ranch Salad</p>
    <p class="t bul" style="left:424px;top:28px">Southwest Latina Salad</p>
    <p class="t bul" style="left:424px;top:46px">Penne Salad</p>
    <p class="t bul" style="left:424px;top:63px">Pea Salad</p>
    <p class="t bul" style="left:424px;top:81px">Broccoli Salad</p>
    <p class="t" style="left:411px;top:101px"><span class="red">Breadsticks</span>&nbsp;&nbsp; $.50 each</p>
    <p class="t" style="left:411px;top:121px"><span class="red">Salad dressings</span>&nbsp;&nbsp; 2oz- $.50</p>
    <p class="t" style="left:500px;top:137px">16oz- $3.00</p>
    <p class="t" style="left:500px;top:152px">32oz- $5.00</p>

    <h2 class="t heading" style="left:550px;top:174px">Desserts</h2>
    <p class="t" style="left:550px;top:204px;transform:translateX(-50%)">Sugar Lane Bakes</p>
    <p class="t red" style="left:411px;top:226px">Menu options</p>
    <p class="t" style="left:411px;top:243px"><span class="red">Cookies</span>&nbsp;&nbsp; $0.75 each</p>
    <p class="t" style="left:411px;top:262px"><span class="red">Brownie</span>&nbsp;&nbsp; $1.25 each</p>
    <p class="t" style="left:411px;top:281px"><span class="red">Blondie</span>&nbsp;&nbsp; $1.25 each</p>
    <p class="t" style="left:411px;top:300px"><span class="red">Pumpkin bar</span>&nbsp; $1.25 each</p>
    <p class="t" style="left:411px;top:319px"><span class="red">Cake Pops</span>&nbsp;&nbsp; $15 per dozen</p>
    <p class="t" style="left:411px;top:344px"><span class="red">Cupcakes</span>&nbsp; $3.25 each or $30 per dozen</p>
    <p class="t" style="left:411px;top:362px"><span class="red">Cake</span>&nbsp; ¼ tray- $25</p>
    <p class="t" style="left:445px;top:382px">½ tray- $45</p>
    <p class="t" style="left:445px;top:401px">Full tray- $85</p>
    <div class="partner-badge" aria-hidden="true"></div>
    <div class="photo" role="img" aria-label="Tiered stand of cupcakes" style="left:682px;top:221px;width:106px;height:194px;background:linear-gradient(180deg,#5a4a40,#8a7464 55%,#d8d2cc)"></div>

    <h2 class="t heading" style="left:601px;top:419px">Information</h2>
    <p class="t red" style="left:411px;top:455px">$100.00 minimum for delivery service</p>
    <p class="t red" style="left:411px;top:475px">1-day minimum notice for delivery</p>

    <p class="t" style="left:411px;top:525px">Ladle and Loaf</p>
    <p class="t" style="left:411px;top:544px">Our locations/info:</p>
    <p class="t" style="left:411px;top:560px">Maple Crossing</p>
    <p class="t" style="left:411px;top:575px">1025 Maple Crossing</p>
    <p class="t" style="left:417px;top:595px"><span class="red">Mon to Sat:</span>&nbsp; 10:30am–9pm</p>
    <p class="t" style="left:456px;top:614px"><span class="red">Sun:</span>&nbsp; 11am–7pm</p>
    <p class="t" style="left:437px;top:633px">(555)-010-1403</p>
    <div class="divider" aria-hidden="true"></div>
    <p class="t" style="left:642px;top:525px">Downtown Riverton</p>
    <p class="t" style="left:642px;top:544px">Our locations/info:</p>
    <p class="t" style="left:642px;top:560px">2481 5th Avenue North</p>
    <p class="t" style="left:642px;top:595px"><span class="red">Mon to Sat:</span>&nbsp; 10:30am–3pm</p>
    <p class="t" style="left:680px;top:614px"><span class="red">Sun:</span>&nbsp; Closed</p>
    <p class="t" style="left:663px;top:633px">(555)-010-0148</p>
    <p class="t" style="left:425px;top:655px"><span class="red">Email:</span> hello@ladleandloaf.com</p>
    <p class="t" style="left:425px;top:673px"><span class="red">Website:</span> www.ladleandloafcatering.com</p>
  </section>

  <div class="brand">Ladle and Loaf</div>
  <div class="photo" role="img" aria-label="Bowls of pasta salad on a salad bar" style="left:833px;top:256px;width:174px;height:157px;background:linear-gradient(135deg,#3c3530,#c9b98a 55%,#6b5a48)"></div>
  <div class="photo" role="img" aria-label="Cupcake display at the shop" style="left:993px;top:294px;width:174px;height:158px;background:linear-gradient(180deg,#e9e4de,#c8b8a8 60%,#5a4030)"></div>
  <div class="photo" role="img" aria-label="Bowl of chili topped with cheese" style="left:895px;top:393px;width:174px;height:157px;background:radial-gradient(circle at 40% 45%,#8a2a18,#b8501e 30%,#f4f1ec 55%,#d9cfc2)"></div>
  <p class="site">www.ladleandloafcatering.com</p>
</main>
</body>
</html>
```